The Bramwellton Shop 2023 PPT

We need our company overview presentation to be updated to look professional and uniform. We would like it to be editable so we can make updates in the future.

```html
<!DOCTYPE html>
<html lang="en">
<head>
<meta charset="utf-8">
<title>The Bramwellton Shop — Company Overview Deck</title>
<link rel="stylesheet" href="https://fonts.googleapis.com/css2?family=Poppins:wght@400;500;600;700;800&display=swap">
<style>
:root{
  --navy:#1b2b4b;
  --navy-deep:#14213b;
  --red:#e3342f;
  --ink:#2b2f38;
  --muted:#7b8190;
  --line:#e3e6ec;
  --soft:#f3f4f7;
  --paper:#ffffff;
  --canvas:#eef0f3;
}
*{box-sizing:border-box;margin:0;padding:0}
html,body{width:1200px;height:3160px;overflow:hidden;background:var(--canvas)}
body{font-family:"Poppins",Arial,sans-serif;color:var(--ink)}
.deck{display:grid;grid-template-columns:540px 540px;grid-auto-rows:288px;column-gap:40px;row-gap:28px;padding:14px 40px}
.slide{position:relative;background:var(--paper);overflow:hidden;box-shadow:0 2px 8px rgba(20,33,59,.08)}
.brand{display:flex;align-items:center;gap:5px;font-weight:700;color:var(--navy);font-size:9px;white-space:nowrap}
.brand-mark{width:9px;height:9px;background:var(--red);display:inline-block}
.slide-head{position:absolute;top:10px;left:16px;right:16px;display:flex;justify-content:space-between;align-items:center}
.slide-tag{font-size:6px;color:var(--muted)}
.slide-foot{position:absolute;left:0;right:0;bottom:0;height:16px;background:var(--navy);display:flex;justify-content:space-between;align-items:center;padding:0 16px;font-size:6px;color:#fff}
.slide-foot::before{content:"";position:absolute;left:0;top:0;width:70px;height:16px;background:var(--red)}
.slide-foot span{position:relative}
.kicker{font-size:7px;font-weight:600;color:var(--red);letter-spacing:.5px;text-transform:uppercase}
.title{font-size:17px;font-weight:700;color:var(--navy);line-height:1.15}
.center{text-align:center}
.small{font-size:6px;color:var(--muted);line-height:1.45}
.photo{position:absolute}
.abs{position:absolute}
.logo-box{background:var(--soft);border:1px solid var(--line);border-radius:3px}
.icon-red{width:26px;height:26px;border-radius:50%;background:var(--red);margin:0 auto 5px;display:flex;align-items:center;justify-content:center}
.icon-line{width:26px;height:26px;border-radius:50%;border:1.5px solid var(--navy);margin:0 auto 5px;display:flex;align-items:center;justify-content:center}
.icon-red svg,.icon-line svg{width:12px;height:12px}
.bullets{list-style:none;font-size:6.5px;color:var(--ink);line-height:1.9}
.bullets li{display:flex;align-items:center;gap:5px}
.bullets li::before{content:"";width:4px;height:4px;background:var(--red);border-radius:50%;flex:none}
.num{width:16px;height:16px;background:var(--red);color:#fff;font-size:7px;font-weight:700;display:flex;align-items:center;justify-content:center;flex:none}
</style>
</head>
<body>
<main class="deck">

<!-- 1 Title -->
<section class="slide">
  <div class="abs brand" style="left:30px;top:60px;font-size:12px"><i class="brand-mark" style="width:12px;height:12px"></i>The Bramwellton Shop</div>
  <div class="abs" style="left:30px;top:110px">
    <h1 class="title" style="font-size:20px">Presentation Title Here</h1>
    <p class="small" style="margin-top:6px">Presentation Subtitle · March 2023</p>
    <p style="font-size:7px;color:var(--red);font-weight:600;margin-top:10px">By: Alex Morrow</p>
  </div>
  <svg class="abs" style="right:0;top:0" width="200" height="288" viewBox="0 0 200 288">
    <polygon points="110,0 200,0 200,288 40,288" fill="var(--navy)"/>
    <polygon points="150,110 200,140 150,170" fill="var(--red)"/>
  </svg>
  <div class="abs small" style="left:30px;bottom:14px">Company Overview 2023</div>
</section>

<!-- 2 Title with photo -->
<section class="slide">
  <div class="abs brand" style="left:30px;top:60px;font-size:12px"><i class="brand-mark" style="width:12px;height:12px"></i>The Bramwellton Shop</div>
  <div class="abs" style="left:30px;top:110px">
    <h1 class="title" style="font-size:20px">Presentation Title Here</h1>
    <p class="small" style="margin-top:6px">Presentation Subtitle · March 2023</p>
    <p style="font-size:7px;color:var(--red);font-weight:600;margin-top:10px">By: Alex Morrow</p>
  </div>
  <div class="photo" role="img" aria-label="Photo of a security professional at work" style="right:0;top:40px;width:230px;height:150px;background:linear-gradient(135deg,#c9ced8,#8a93a6);clip-path:polygon(25% 0,100% 0,100% 100%,0 100%)"></div>
  <svg class="abs" style="right:20px;top:170px" width="60" height="60"><polygon points="0,0 60,30 0,60" fill="var(--red)"/></svg>
  <div class="slide-foot"><span>The Bramwellton Shop</span><span>01</span></div>
</section>

<!-- 3 National presence -->
<section class="slide">
  <div class="slide-head"><span class="brand"><i class="brand-mark"></i>The Bramwellton Shop</span><span class="slide-tag">Company Overview</span></div>
  <div class="abs" style="left:24px;top:120px;width:170px">
    <p class="kicker">Locations</p>
    <h2 class="title" style="font-size:19px">Our National Presence</h2>
    <p class="small" style="margin-top:6px">Regional offices with coast to coast reach</p>
  </div>
  <div class="photo" role="img" aria-label="Map of national office locations" style="left:210px;top:36px;width:310px;height:220px;background:linear-gradient(160deg,#dfe3ea,#bcc3d0);border-radius:4px"></div>
  <div class="slide-foot"><span>The Bramwellton Shop</span><span>02</span></div>
</section>

<!-- 4 Technology difference -->
<section class="slide">
  <div class="slide-head"><span class="brand"><i class="brand-mark"></i>The Bramwellton Shop</span><span class="slide-tag">Company Overview</span></div>
  <div class="abs center" style="left:0;right:0;top:34px"><p class="kicker">Why Us</p><h2 class="title">The Technology Difference</h2></div>
  <div class="abs" style="left:30px;right:30px;top:92px;display:grid;grid-template-columns:repeat(6,1fr);gap:6px;text-align:center">
    <div><div class="icon-red"><svg viewBox="0 0 12 12"><rect x="2" y="3" width="8" height="6" fill="#fff"/></svg></div><p class="small">Video Systems</p></div>
    <div><div class="icon-red"><svg viewBox="0 0 12 12"><circle cx="6" cy="6" r="3.5" fill="#fff"/></svg></div><p class="small">Access Control</p></div>
    <div><div class="icon-red"><svg viewBox="0 0 12 12"><path d="M2 6l3 3 5-6" stroke="#fff" stroke-width="1.6" fill="none"/></svg></div><p class="small">Intrusion Alarms</p></div>
    <div><div class="icon-red"><svg viewBox="0 0 12 12"><rect x="2" y="2" width="8" height="8" rx="1" fill="#fff"/></svg></div><p class="small">Cloud Hosting</p></div>
    <div><div class="icon-red"><svg viewBox="0 0 12 12"><path d="M6 1l5 9H1z" fill="#fff"/></svg></div><p class="small">Analytics</p></div>
    <div><div class="icon-red"><svg viewBox="0 0 12 12"><circle cx="6" cy="6" r="4" stroke="#fff" stroke-width="1.5" fill="none"/></svg></div><p class="small">Remote Support</p></div>
  </div>
  <div class="abs" style="left:60px;right:60px;top:172px;display:grid;grid-template-columns:repeat(5,1fr);gap:6px;text-align:center">
    <div><div class="icon-line"><svg viewBox="0 0 12 12"><circle cx="6" cy="6" r="3" fill="var(--navy)"/></svg></div><p class="small">Design Team</p></div>
    <div><div class="icon-line"><svg viewBox="0 0 12 12"><rect x="3" y="3" width="6" height="6" fill="var(--navy)"/></svg></div><p class="small">Certified Installers</p></div>
    <div><div class="icon-line"><svg viewBox="0 0 12 12"><path d="M2 6l3 3 5-6" stroke="var(--navy)" stroke-width="1.6" fill="none"/></svg></div><p class="small">Project Managers</p></div>
    <div><div class="icon-line"><svg viewBox="0 0 12 12"><path d="M6 2l4 8H2z" fill="var(--navy)"/></svg></div><p class="small">Service Desk</p></div>
    <div><div class="icon-line"><svg viewBox="0 0 12 12"><circle cx="6" cy="6" r="3.5" stroke="var(--navy)" stroke-width="1.4" fill="none"/></svg></div><p class="small">Field Technicians</p></div>
  </div>
  <div class="slide-foot"><span>The Bramwellton Shop</span><span>03</span></div>
</section>

<!-- 5 People difference -->
<section class="slide">
  <div class="abs" style="left:0;top:0;bottom:0;width:170px;background:var(--navy);padding:70px 18px 0">
    <h2 class="title" style="color:#fff;font-size:18px">The People Difference</h2>
    <p class="small" style="color:#c6cce0;margin-top:8px">Our team brings decades of hands on field and design experience to every project.</p>
  </div>
  <div class="abs" style="left:186px;right:16px;top:30px;display:grid;grid-template-columns:repeat(3,1fr);gap:7px 8px">
    <div class="small"><b style="color:var(--navy)">Engineering</b><br>Licensed system designers</div>
    <div class="small"><b style="color:var(--navy)">Installation</b><br>Certified field crews</div>
    <div class="small"><b style="color:var(--navy)">Service</b><br>Around the clock response</div>
    <div class="small"><b style="color:var(--navy)">Training</b><br>Onsite user sessions</div>
    <div class="small"><b style="color:var(--navy)">Safety</b><br>Industry safety tickets</div>
    <div class="small"><b style="color:var(--navy)">Security</b><br>Cleared staff members</div>
    <div class="small"><b style="color:var(--navy)">Support</b><br>Dedicated account leads</div>
    <div class="small"><b style="color:var(--navy)">Quality</b><br>Audited install process</div>
    <div class="small"><b style="color:var(--navy)">Reporting</b><br>Clear project updates</div>
    <div class="small"><b style="color:var(--navy)">Planning</b><br>Site surveys and scoping</div>
    <div class="small"><b style="color:var(--navy)">Networks</b><br>IT and cabling experts</div>
    <div class="small"><b style="color:var(--navy)">Monitoring</b><br>Remote health checks</div>
    <div class="small"><b style="color:var(--navy)">Compliance</b><br>Code and permit ready</div>
    <div class="small"><b style="color:var(--navy)">Logistics</b><br>National parts stock</div>
    <div class="small"><b style="color:var(--navy)">Care</b><br>Long term partnerships</div>
  </div>
  <div class="slide-foot"><span>The Bramwellton Shop</span><span>04</span></div>
</section>

<!-- 6 Industries -->
<section class="slide">
  <div class="slide-head"><span class="brand"><i class="brand-mark"></i>The Bramwellton Shop</span><span class="slide-tag">Company Overview</span></div>
  <div class="abs center" style="left:0;right:0;top:30px"><h2 class="title" style="font-size:14px">25 Years Experience In The Following Industries</h2></div>
  <div class="abs" style="left:24px;right:24px;top:62px;display:grid;grid-template-columns:80px repeat(5,1fr);gap:7px;align-items:center;grid-auto-rows:30px">
    <p class="small" style="color:var(--navy);font-weight:600">Logistics</p><div class="logo-box" style="height:100%"></div><div class="logo-box" style="height:100%"></div><div class="logo-box" style="height:100%"></div><div class="logo-box" style="height:100%"></div><div class="logo-box" style="height:100%"></div>
    <p class="small" style="color:var(--navy);font-weight:600">Retail Stores</p><div class="logo-box" style="height:100%"></div><div class="logo-box" style="height:100%"></div><div class="logo-box" style="height:100%"></div><div class="logo-box" style="height:100%"></div><div class="logo-box" style="height:100%"></div>
    <p class="small" style="color:var(--navy);font-weight:600">Hospitality</p><div class="logo-box" style="height:100%"></div><div class="logo-box" style="height:100%"></div><div class="logo-box" style="height:100%"></div><div class="logo-box" style="height:100%"></div><div class="logo-box" style="height:100%"></div>
    <p class="small" style="color:var(--navy);font-weight:600">Property</p><div class="logo-box" style="height:100%"></div><div class="logo-box" style="height:100%"></div><div class="logo-box" style="height:100%"></div><div class="logo-box" style="height:100%"></div><div class="logo-box" style="height:100%"></div>
    <p class="small" style="color:var(--navy);font-weight:600">Government</p><div class="logo-box" style="height:100%"></div><div class="logo-box" style="height:100%"></div><div class="logo-box" style="height:100%"></div><div class="logo-box" style="height:100%"></div><div class="logo-box" style="height:100%"></div>
  </div>
  <div class="slide-foot"><span>The Bramwellton Shop</span><span>05</span></div>
</section>

<!-- 7 Industries cont. -->
<section class="slide">
  <div class="slide-head"><span class="brand"><i class="brand-mark"></i>The Bramwellton Shop</span><span class="slide-tag">Company Overview</span></div>
  <div class="abs center" style="left:0;right:0;top:30px"><h2 class="title" style="font-size:14px">25 Years Experience In The Following Industries</h2></div>
  <div class="abs" style="left:24px;right:24px;top:62px;display:grid;grid-template-columns:80px repeat(5,1fr);gap:7px;align-items:center;grid-auto-rows:30px">
    <p class="small" style="color:var(--navy);font-weight:600">Education</p><div class="logo-box" style="height:100%"></div><div class="logo-box" style="height:100%"></div><div class="logo-box" style="height:100%"></div><div class="logo-box" style="height:100%"></div><div class="logo-box" style="height:100%"></div>
    <p class="small" style="color:var(--navy);font-weight:600">Banks and Insurance</p><div class="logo-box" style="height:100%"></div><div class="logo-box" style="height:100%"></div><div class="logo-box" style="height:100%"></div><div class="logo-box" style="height:100%"></div><div class="logo-box" style="height:100%"></div>
    <p class="small" style="color:var(--navy);font-weight:600">Healthcare</p><div class="logo-box" style="height:100%"></div><div class="logo-box" style="height:100%"></div><div class="logo-box" style="height:100%"></div><div class="logo-box" style="height:100%"></div><div class="logo-box" style="height:100%"></div>
    <p class="small" style="color:var(--navy);font-weight:600">Industrial</p><div class="logo-box" style="height:100%"></div><div class="logo-box" style="height:100%"></div><div class="logo-box" style="height:100%"></div><div class="logo-box" style="height:100%"></div><div class="logo-box" style="height:100%"></div>
    <p class="small" style="color:var(--navy);font-weight:600">Transit</p><div class="logo-box" style="height:100%"></div><div class="logo-box" style="height:100%"></div><div class="logo-box" style="height:100%"></div><div class="logo-box" style="height:100%"></div><div class="logo-box" style="height:100%"></div>
  </div>
  <div class="slide-foot"><span>The Bramwellton Shop</span><span>06</span></div>
</section>

<!-- 8 Oil and gas -->
<section class="slide">
  <div class="slide-head"><span class="brand"><i class="brand-mark"></i>The Bramwellton Shop</span><span class="slide-tag">Company Overview</span></div>
  <div class="abs center" style="left:0;right:0;top:34px"><p class="kicker">Energy Sector</p><h2 class="title">Oil and Gas Customers</h2></div>
  <div class="abs" style="left:40px;right:40px;top:92px;display:grid;grid-template-columns:repeat(5,1fr);grid-auto-rows:40px;gap:12px">
    <div class="logo-box"></div><div class="logo-box"></div><div class="logo-box"></div><div class="logo-box"></div><div class="logo-box"></div>
    <div class="logo-box"></div><div class="logo-box"></div><div class="logo-box"></div><div class="logo-box"></div><div class="logo-box"></div>
    <div class="logo-box"></div><div class="logo-box"></div><div class="logo-box"></div><div class="logo-box"></div><div class="logo-box"></div>
  </div>
  <div class="slide-foot"><span>The Bramwellton Shop</span><span>07</span></div>
</section>

<!-- 9 Key partners -->
<section class="slide">
  <div class="slide-head"><span class="brand"><i class="brand-mark"></i>The Bramwellton Shop</span><span class="slide-tag">Company Overview</span></div>
  <div class="abs center" style="left:0;right:0;top:34px"><p class="kicker">Partners</p><h2 class="title">Our Key Partners</h2></div>
  <div class="abs" style="left:40px;right:40px;top:86px;display:grid;grid-template-columns:repeat(5,1fr);grid-auto-rows:32px;gap:10px">
    <div class="logo-box"></div><div class="logo-box"></div><div class="logo-box"></div><div class="logo-box"></div><div class="logo-box"></div>
    <div class="logo-box"></div><div class="logo-box"></div><div class="logo-box"></div><div class="logo-box"></div><div class="logo-box"></div>
    <div class="logo-box"></div><div class="logo-box"></div><div class="logo-box"></div><div class="logo-box"></div><div class="logo-box"></div>
    <div class="logo-box"></div><div class="logo-box"></div><div class="logo-box"></div><div class="logo-box"></div><div class="logo-box"></div>
  </div>
  <div class="slide-foot"><span>The Bramwellton Shop</span><span>08</span></div>
</section>

<!-- 10 Access control intro -->
<section class="slide">
  <div class="slide-head"><span class="brand"><i class="brand-mark"></i>The Bramwellton Shop</span><span class="slide-tag">Company Overview</span></div>
  <div class="photo" role="img" aria-label="Photo of a staff member holding a red folder" style="left:24px;top:36px;width:200px;height:220px;background:linear-gradient(160deg,#d9dde5,#9aa2b3);border-radius:4px"></div>
  <div class="abs" style="left:244px;right:24px;top:44px">
    <p class="kicker">Solutions</p>
    <h2 class="title" style="font-size:16px">Harrowgate Access Control System</h2>
    <div style="margin-top:14px;display:flex;flex-direction:column;gap:14px">
      <div style="display:flex;gap:8px"><span class="num">1</span><p class="small">Secure doors, gates and lifts from one central platform with clear audit trails.</p></div>
      <div style="display:flex;gap:8px"><span class="num">2</span><p class="small">Scales from a single site to a national estate with shared card holders.</p></div>
      <div style="display:flex;gap:8px"><span class="num">3</span><p class="small">Links with video and alarms so every event is seen and acted on fast.</p></div>
    </div>
  </div>
  <div class="slide-foot"><span>The Bramwellton Shop</span><span>09</span></div>
</section>

<!-- 11 Access control list -->
<section class="slide">
  <div class="slide-head"><span class="brand"><i class="brand-mark"></i>The Bramwellton Shop</span><span class="slide-tag">Company Overview</span></div>
  <div class="abs" style="left:24px;top:32px"><p class="kicker">Features</p><h2 class="title" style="font-size:14px">Harrowgate Access Control System</h2></div>
  <div class="abs" style="left:24px;top:78px;width:330px;display:grid;grid-template-columns:1fr 1fr;gap:0 12px">
    <ul class="bullets"><li>Card and mobile access</li><li>Visitor management</li><li>Lockdown on demand</li><li>Alarm integration</li><li>Time based schedules</li><li>Elevator control</li><li>Muster reporting</li><li>Audit trail exports</li></ul>
    <ul class="bullets"><li>Central web console</li><li>Multi site support</li><li>Photo ID badges</li><li>Anti passback rules</li><li>Video event linking</li><li>Encrypted readers</li><li>Offline door modes</li><li>Role based rights</li></ul>
  </div>
  <div class="photo" role="img" aria-label="Photo of a dome security camera" style="right:0;top:30px;width:160px;height:242px;background:linear-gradient(180deg,#2a3b5e,var(--navy-deep))"></div>
  <div class="slide-foot"><span>The Bramwellton Shop</span><span>10</span></div>
</section>

<!-- 12 Access control list 2 -->
<section class="slide">
  <div class="slide-head"><span class="brand"><i class="brand-mark"></i>The Bramwellton Shop</span><span class="slide-tag">Company Overview</span></div>
  <div class="abs" style="left:24px;top:32px"><p class="kicker">Features</p><h2 class="title" style="font-size:14px">Harrowgate Access Control System</h2></div>
  <div class="abs" style="left:24px;top:78px;width:330px;display:grid;grid-template-columns:1fr 1fr;gap:0 12px">
    <ul class="bullets"><li>Intuitive software</li><li>Live door status</li><li>Remote unlock</li><li>Guard tour logs</li><li>Custom reports</li><li>Threat levels</li></ul>
    <ul class="bullets"><li>Intercom support</li><li>Biometric readers</li><li>Key cabinets</li><li>Perimeter fences</li><li>Parking gates</li><li>Cloud backups</li></ul>
  </div>
  <div class="photo" role="img" aria-label="Photo of security cameras and reader hardware" style="right:24px;top:60px;width:150px;height:180px;background:linear-gradient(160deg,#f1f2f5,#cfd4dd);border-radius:4px"></div>
  <div class="slide-foot"><span>The Bramwellton Shop</span><span>11</span></div>
</section>

<!-- 13 Camera solution icons -->
<section class="slide">
  <div class="slide-head"><span class="brand"><i class="brand-mark"></i>The Bramwellton Shop</span><span class="slide-tag">Company Overview</span></div>
  <div class="abs center" style="left:0;right:0;top:30px"><h2 class="title" style="font-size:15px">Corvane Solutions Camera Solution</h2></div>
  <div class="abs" style="left:30px;right:30px;top:66px;display:grid;grid-template-columns:repeat(6,1fr);gap:6px;text-align:center">
    <div><div class="icon-line"><svg viewBox="0 0 12 12"><rect x="2" y="3" width="8" height="6" fill="var(--navy)"/></svg></div><p class="small">HD Video</p></div>
    <div><div class="icon-line"><svg viewBox="0 0 12 12"><circle cx="6" cy="6" r="3" fill="var(--navy)"/></svg></div><p class="small">Smart Search</p></div>
    <div><div class="icon-line"><svg viewBox="0 0 12 12"><path d="M2 6l3 3 5-6" stroke="var(--navy)" stroke-width="1.6" fill="none"/></svg></div><p class="small">Alerts</p></div>
    <div><div class="icon-line"><svg viewBox="0 0 12 12"><path d="M6 2l4 8H2z" fill="var(--navy)"/></svg></div><p class="small">Night Vision</p></div>
    <div><div class="icon-line"><svg viewBox="0 0 12 12"><rect x="3" y="3" width="6" height="6" fill="var(--navy)"/></svg></div><p class="small">Storage</p></div>
    <div><div class="icon-line"><svg viewBox="0 0 12 12"><circle cx="6" cy="6" r="3.5" stroke="var(--navy)" stroke-width="1.4" fill="none"/></svg></div><p class="small">Mobile App</p></div>
  </div>
  <div class="abs center" style="left:0;right:0;top:140px"><p style="font-size:8px;font-weight:600;color:var(--navy)">Foundation and Differentiators</p></div>
  <div class="abs" style="left:60px;right:60px;top:162px;display:grid;grid-template-columns:repeat(5,1fr);gap:6px;text-align:center">
    <div><div class="icon-red"><svg viewBox="0 0 12 12"><circle cx="6" cy="6" r="3" fill="#fff"/></svg></div><p class="small">Open Platform</p></div>
    <div><div class="icon-red"><svg viewBox="0 0 12 12"><rect x="3" y="3" width="6" height="6" fill="#fff"/></svg></div><p class="small">Cyber Secure</p></div>
    <div><div class="icon-red"><svg viewBox="0 0 12 12"><path d="M2 6l3 3 5-6" stroke="#fff" stroke-width="1.6" fill="none"/></svg></div><p class="small">Easy Setup</p></div>
    <div><div class="icon-red"><svg viewBox="0 0 12 12"><path d="M6 2l4 8H2z" fill="#fff"/></svg></div><p class="small">Analytics</p></div>
    <div><div class="icon-red"><svg viewBox="0 0 12 12"><circle cx="6" cy="6" r="3.5" stroke="#fff" stroke-width="1.4" fill="none"/></svg></div><p class="small">Scalable</p></div>
  </div>
  <div class="slide-foot"><span>The Bramwellton Shop</span><span>12</span></div>
</section>

<!-- 14 Camera solution products -->
<section class="slide">
  <div class="slide-head"><span class="brand"><i class="brand-mark"></i>The Bramwellton Shop</span><span class="slide-tag">Company Overview</span></div>
  <div class="abs" style="left:24px;top:30px"><h2 class="title" style="font-size:15px">Corvane Solutions Camera Solution</h2></div>
  <div class="photo" role="img" aria-label="Photos of dome and bullet security cameras" style="left:24px;top:66px;width:230px;height:190px;background:linear-gradient(160deg,#f0f1f4,#c4cad5);border-radius:4px"></div>
  <div class="abs" style="left:276px;right:24px;top:70px;display:flex;flex-direction:column;gap:16px">
    <div><p style="font-size:8px;font-weight:600;color:var(--red)">Fixed Cameras</p><p class="small">Sharp image quality for indoor and outdoor coverage.</p></div>
    <div><p style="font-size:8px;font-weight:600;color:var(--red)">Multi Sensor Cameras</p><p class="small">Wide area views from a single mounting point.</p></div>
    <div><p style="font-size:8px;font-weight:600;color:var(--red)">Video Management</p><p class="small">Record, search and share footage from any device.</p></div>
  </div>
  <div class="slide-foot"><span>The Bramwellton Shop</span><span>13</span></div>
</section>

<!-- 15 Camera solution grid -->
<section class="slide">
  <div class="slide-head"><span class="brand"><i class="brand-mark"></i>The Bramwellton Shop</span><span class="slide-tag">Company Overview</span></div>
  <div class="abs center" style="left:0;right:0;top:30px"><h2 class="title" style="font-size:15px">Corvane Solutions Camera Solution</h2></div>
  <div class="abs" style="left:40px;right:40px;top:70px;display:grid;grid-template-columns:repeat(3,1fr);gap:14px 20px;text-align:center">
    <div><div class="icon-line"><svg viewBox="0 0 12 12"><rect x="2" y="3" width="8" height="6" fill="var(--navy)"/></svg></div><p class="small">Live view on any screen</p></div>
    <div><div class="icon-line"><svg viewBox="0 0 12 12"><circle cx="6" cy="6" r="3" fill="var(--navy)"/></svg></div><p class="small">Motion based search</p></div>
    <div><div class="icon-line"><svg viewBox="0 0 12 12"><path d="M2 6l3 3 5-6" stroke="var(--navy)" stroke-width="1.6" fill="none"/></svg></div><p class="small">Verified alarm events</p></div>
    <div><div class="icon-line"><svg viewBox="0 0 12 12"><path d="M6 2l4 8H2z" fill="var(--navy)"/></svg></div><p class="small">Licence plate reading</p></div>
    <div><div class="icon-line"><svg viewBox="0 0 12 12"><rect x="3" y="3" width="6" height="6" fill="var(--navy)"/></svg></div><p class="small">Redundant recording</p></div>
    <div><div class="icon-line"><svg viewBox="0 0 12 12"><circle cx="6" cy="6" r="3.5" stroke="var(--navy)" stroke-width="1.4" fill="none"/></svg></div><p class="small">Health monitoring</p></div>
    <div><div class="icon-line"><svg viewBox="0 0 12 12"><circle cx="6" cy="6" r="2" fill="var(--navy)"/></svg></div><p class="small">Privacy masking</p></div>
    <div><div class="icon-line"><svg viewBox="0 0 12 12"><rect x="2" y="5" width="8" height="2" fill="var(--navy)"/></svg></div><p class="small">Evidence export</p></div>
    <div><div class="icon-line"><svg viewBox="0 0 12 12"><path d="M3 3h6v6H3z" stroke="var(--navy)" fill="none"/></svg></div><p class="small">Role based access</p></div>
  </div>
  <div class="slide-foot"><span>The Bramwellton Shop</span><span>14</span></div>
</section>

<!-- 16 Camera solution photos -->
<section class="slide">
  <div class="slide-head"><span class="brand"><i class="brand-mark"></i>The Bramwellton Shop</span><span class="slide-tag">Company Overview</span></div>
  <div class="abs center" style="left:0;right:0;top:30px"><h2 class="title" style="font-size:15px">Corvane Solutions Camera Solution</h2></div>
  <div class="abs" style="left:30px;right:30px;top:64px;display:grid;grid-template-columns:repeat(3,1fr);gap:14px">
    <div><p style="font-size:8px;font-weight:600;color:var(--navy)">Body Worn</p><p class="small">Cameras for patrol teams on the move.</p></div>
    <div><p style="font-size:8px;font-weight:600;color:var(--navy)">Fleet Video</p><p class="small">Recording for vehicles across the route.</p></div>
    <div><p style="font-size:8px;font-weight:600;color:var(--navy)">Site Trailers</p><p class="small">Mobile towers for remote job sites.</p></div>
    <div class="photo" role="img" aria-label="Photo of a body worn camera" style="position:static;height:130px;background:linear-gradient(160deg,#cdd2db,#8d96a8);border-radius:4px"></div>
    <div class="photo" role="img" aria-label="Photo of a vehicle camera" style="position:static;height:130px;background:linear-gradient(160deg,#cdd2db,#8d96a8);border-radius:4px"></div>
    <div class="photo" role="img" aria-label="Photo of a mobile surveillance tower" style="position:static;height:130px;background:linear-gradient(160deg,#cdd2db,#8d96a8);border-radius:4px"></div>
  </div>
  <div class="slide-foot"><span>The Bramwellton Shop</span><span>15</span></div>
</section>

<!-- 17 Service plans -->
<section class="slide">
  <div class="slide-head"><span class="brand"><i class="brand-mark"></i>The Bramwellton Shop</span><span class="slide-tag">Company Overview</span></div>
  <div class="abs" style="left:24px;top:30px"><h2 class="title" style="font-size:15px">Custom Service and Maintenance Plans</h2></div>
  <div class="abs" style="left:24px;right:24px;top:66px;display:grid;grid-template-columns:repeat(3,1fr);grid-auto-rows:56px;gap:9px">
    <div class="logo-box" style="padding:8px;display:flex;gap:7px;align-items:center"><span class="num">1</span><p class="small">Preventive inspections</p></div>
    <div class="logo-box" style="padding:8px;display:flex;gap:7px;align-items:center"><span class="num">2</span><p class="small">Priority response</p></div>
    <div class="logo-box" style="padding:8px;display:flex;gap:7px;align-items:center"><span class="num">3</span><p class="small">Firmware updates</p></div>
    <div class="logo-box" style="padding:8px;display:flex;gap:7px;align-items:center"><span class="num">4</span><p class="small">Parts coverage</p></div>
    <div class="logo-box" style="padding:8px;display:flex;gap:7px;align-items:center"><span class="num">5</span><p class="small">Remote diagnostics</p></div>
    <div class="logo-box" style="padding:8px;display:flex;gap:7px;align-items:center"><span class="num">6</span><p class="small">User training</p></div>
    <div class="logo-box" style="padding:8px;display:flex;gap:7px;align-items:center"><span class="num">7</span><p class="small">System health reports</p></div>
    <div class="logo-box" style="padding:8px;display:flex;gap:7px;align-items:center"><span class="num">8</span><p class="small">Upgrade planning</p></div>
    <div class="logo-box" style="padding:8px;display:flex;gap:7px;align-items:center"><span class="num">9</span><p class="small">Annual reviews</p></div>
  </div>
  <div class="slide-foot"><span>The Bramwellton Shop</span><span>16</span></div>
</section>

<!-- 18 Dark company summary -->
<section class="slide" style="background:var(--navy-deep)">
  <div class="abs brand" style="left:16px;top:10px;color:#fff"><i class="brand-mark"></i>The Bramwellton Shop</div>
  <div class="abs" style="left:30px;top:44px"><p class="kicker">Who We Are</p><h2 class="title" style="color:#fff;font-size:18px;letter-spacing:.5px">THE BRAMWELLTON SHOP</h2></div>
  <div class="abs" style="left:30px;right:30px;top:106px;display:grid;grid-template-columns:repeat(4,1fr);gap:16px 14px">
    <div><i class="brand-mark" style="display:block;margin-bottom:5px"></i><p class="small" style="color:#c6cce0">Founded over 25 years ago</p></div>
    <div><i class="brand-mark" style="display:block;margin-bottom:5px"></i><p class="small" style="color:#c6cce0">Offices across the country</p></div>
    <div><i class="brand-mark" style="display:block;margin-bottom:5px"></i><p class="small" style="color:#c6cce0">Certified technical staff</p></div>
    <div><i class="brand-mark" style="display:block;margin-bottom:5px"></i><p class="small" style="color:#c6cce0">Full design to service</p></div>
    <div><i class="brand-mark" style="display:block;margin-bottom:5px"></i><p class="small" style="color:#c6cce0">Trusted by major brands</p></div>
    <div><i class="brand-mark" style="display:block;margin-bottom:5px"></i><p class="small" style="color:#c6cce0">Open platform approach</p></div>
    <div><i class="brand-mark" style="display:block;margin-bottom:5px"></i><p class="small" style="color:#c6cce0">Around the clock support</p></div>
    <div><i class="brand-mark" style="display:block;margin-bottom:5px"></i><p class="small" style="color:#c6cce0">Long term partnerships</p></div>
  </div>
  <div class="abs" style="left:0;right:0;bottom:0;height:4px;background:var(--red)"></div>
</section>

<!-- 19 Brand slide -->
<section class="slide">
  <div class="abs" style="left:0;right:0;top:0;bottom:0;display:flex;align-items:center;justify-content:center;gap:14px">
    <i class="brand-mark" style="width:34px;height:34px"></i>
    <span style="font-size:30px;font-weight:700;color:var(--navy)">The Bramwellton Shop</span>
  </div>
</section>

<!-- 20 Thank you -->
<section class="slide">
  <div class="abs center" style="left:0;right:0;top:80px">
    <div class="brand" style="justify-content:center;font-size:10px"><i class="brand-mark"></i>The Bramwellton Shop</div>
    <h2 class="title" style="font-size:30px;margin-top:14px">Thank You</h2>
    <p class="small" style="margin-top:6px">Questions and discussion</p>
  </div>
  <div class="slide-foot"><span>The Bramwellton Shop</span><span>17</span></div>
</section>

</main>
</body>
</html>
```